Design a New Site for a very cool Watch

We have the overall design element of the website and the banners in the PSD file. We need someone to finish our design in PSD and than convert to HTML. We have included the instructions, PSD file, images and all text.

We currently use Hubspot to host and make changes to our site. The entire design aspect is complete so all we need is some minor changes and additions within the photoshop design and than the coding into HTML.

Please only sign up if you understand photoshop and HTML conversion

Here is the DropBox link to the files
https://files.quorvel-share.net/s/pm4kx82lwq7dtne/Belthor%20Site.zip
Updates

We have the basic design concept in Photoshop.  We just need someone who can complete some changes, make some additions and convert to HTML

Target Market(s)

Watch Buyers

Requirements
Must have
• Must look like a professional luxury brand

Our brand colors are very basic with Black, White and Grey can be used

```html
<!DOCTYPE html>
<html lang="en">
<head>
<meta charset="utf-8">
<title>Belthor &amp; Co. — Watches</title>
<link rel="stylesheet" href="https://fonts.googleapis.com/css2?family=Questrial&family=PT+Sans:wght@400;700&display=swap">
<style>
  :root {
    --orange: #ff6a2b;
    --green: #98b41b;
    --yellow: #ffb400;
    --grey-nav: #e1e1e1;
    --grey-panel: #e6e6e6;
    --grey-footer: #cccccc;
    --grey-base: #a9a9a9;
    --ink: #111111;
    --folk: #3a5a9b;
    --chirp: #4a86c6;
    --reel: #d13a2a;
    --head: "Questrial", sans-serif;
    --body: "PT Sans", sans-serif;
  }
  * { box-sizing: border-box; margin: 0; padding: 0; }
  html, body { width: 1200px; height: 1023px; overflow: hidden; background: #fff; }
  .page { position: relative; width: 1200px; height: 1023px; font-family: var(--body); color: var(--ink); }
  .abs { position: absolute; }

  .top-rule { left: 0; top: 0; width: 1200px; height: 4px; background: var(--orange); }

  .brand { left: 161px; top: 19px; height: 42px; display: flex; align-items: center; gap: 12px; }
  .brand-mark { width: 36px; height: 36px; background: var(--ink); }
  .brand-name { font-family: var(--head); font-size: 29px; letter-spacing: 0.5px; color: var(--ink); }
  .cart { left: 890px; top: 43px; font-family: var(--body); font-size: 14px; }
  .cart span { color: var(--green); }

  .nav { left: 0; top: 83px; width: 1200px; height: 49px; background: var(--grey-nav); border-top: 4px solid #d2d2d2; }
  .nav ul { list-style: none; position: absolute; left: 161px; top: -4px; display: flex; height: 49px; }
  .nav li { height: 49px; display: flex; align-items: center; justify-content: center; font-size: 16px; border-right: 1px solid #c9c9c9; }
  .nav li.active { background: var(--yellow); color: #fff; }

  .hero { left: 0; top: 132px; width: 1200px; height: 342px;
    background: linear-gradient(90deg, #1b1f45 0%, #0d0d10 10%, #3a2410 25%, #6a3a12 45%, #2a1608 60%, #0a0a0a 72%, #2a1f3a 90%, #0a0a0a 100%); }
  .hero-photo { left: 650px; top: 14px; width: 316px; height: 320px; border-radius: 40px;
    background: radial-gradient(circle at 50% 45%, #e31b1b 0%, #a80f0f 45%, #1e1e1e 70%, rgba(0,0,0,0) 72%); }
  .hero-panel { left: 211px; top: 55px; width: 404px; height: 287px; background: rgba(0,0,0,0.35); }
  .hero-title { left: 226px; top: 73px; font-family: var(--head); font-size: 27px; color: #fff; letter-spacing: 0.5px; }
  .hero-copy { left: 229px; top: 125px; width: 385px; font-size: 15px; line-height: 25.5px; color: #fff; }
  .hero-btn { left: 231px; top: 246px; width: 144px; height: 44px; background: #fff; border-radius: 6px;
    font-family: var(--body); font-weight: 700; font-size: 19px; display: flex; align-items: center; justify-content: center; }
  .hero-arrow { top: 132px; }

  .tile { top: 495px; height: 209px; }
  .tile-photo { top: 495px; height: 209px; }
  .tile-text { color: #fff; padding: 14px 0 0 15px; }
  .tile-head { font-family: var(--head); line-height: 1.05; }
  .tile-note { position: absolute; left: 15px; bottom: 14px; font-size: 12.5px; line-height: 18px; }

  .register { left: 161px; top: 733px; width: 583px; height: 173px; background: var(--grey-panel); }
  .reg-title { left: 19px; top: 19px; font-family: var(--head); font-size: 23px; line-height: 29px; }
  .reg-title span { color: var(--orange); }
  .field { top: 84px; height: 34px; background: #fff; border: 1px solid #cfcfcf; font-size: 13.5px; color: #666; padding: 8px 0 0 14px; }
  .login { left: 443px; top: 86px; width: 109px; height: 33px; background: var(--green); border: 2px solid #b4cf3a; border-radius: 4px;
    font-size: 14px; display: flex; align-items: center; justify-content: center; color: #1f2a00; }
  .signup { left: 21px; top: 128px; font-size: 14px; }
  .signup span { color: var(--green); }

  .social { left: 798px; height: 49px; display: flex; align-items: center; }
  .social-box { width: 49px; height: 49px; }
  .social-name { margin-left: 25px; font-family: var(--head); font-size: 28px; }

  .footer { left: 0; top: 942px; width: 1200px; height: 68px; background: var(--grey-footer); }
  .footer-base { left: 0; top: 1010px; width: 1200px; height: 13px; background: var(--grey-base); }
  .footer-links { left: 0; top: 17px; width: 1200px; display: flex; justify-content: center; font-size: 11.5px; gap: 15px; }
  .footer-copy { left: 0; top: 44px; width: 1200px; text-align: center; font-size: 11.5px; }
  .footer-copy span { color: var(--orange); }
</style>
</head>
<body>
<div class="page">
  <div class="abs top-rule"></div>

  <header>
    <div class="abs brand"><div class="brand-mark"></div><div class="brand-name">BELTHOR &amp; CO.</div></div>
    <div class="abs cart"><span>Cart :</span> 0 items(s) - $0.00</div>
  </header>

  <nav class="abs nav">
    <ul>
      <li class="active" style="width:95px">Home</li>
      <li style="width:124px">About Us</li>
      <li style="width:141px">Collecation</li>
      <li style="width:110px">Life Style</li>
      <li style="width:107px">Media</li>
      <li style="width:138px">Shop Now</li>
      <li style="width:162px">Contact Us</li>
    </ul>
  </nav>

  <section class="abs hero">
    <div class="abs hero-photo" role="img" aria-label="Square watch with red face and red strap"></div>
    <div class="abs hero-panel"></div>
    <h1 class="abs hero-title" style="font-weight:400">BUSINESS SOLUTIONS</h1>
    <p class="abs hero-copy">Lorem Ipsum is simply dummy text of the printing and typesetting industry. Lorem.Lorem Ipsum is simply dummy text of the printing and typesetting industry. LoremLorem.</p>
    <div class="abs hero-btn">SEE MORE</div>
    <svg class="abs hero-arrow" style="left:180px" width="20" height="80" viewBox="0 0 20 80"><polyline points="18,2 2,40 18,78" fill="none" stroke="#fff" stroke-width="1.5"/></svg>
    <svg class="abs hero-arrow" style="left:992px" width="20" height="80" viewBox="0 0 20 80"><polyline points="2,2 18,40 2,78" fill="none" stroke="#fff" stroke-width="1.5"/></svg>
  </section>

  <section class="promos">
    <div class="abs tile-photo" style="left:161px;width:115px;background:linear-gradient(135deg,#0c1a3a,#2a4fa0 55%,#0a0a0a)" role="img" aria-label="Blue watch close-up"></div>
    <div class="abs tile tile-text" style="left:276px;width:175px;background:var(--green)">
      <div class="tile-head" style="font-size:38px;line-height:46px">THE<br>NOVA<br>STORY</div>
      <div class="tile-note">Lorem Ipsum is<br>simply dummy text of the</div>
    </div>

    <div class="abs tile-photo" style="left:454px;width:121px;background:linear-gradient(135deg,#d9d9d9,#f4f4f4 50%,#8a8a8a)" role="img" aria-label="White watch with pink details"></div>
    <div class="abs tile tile-text" style="left:575px;width:169px;background:var(--yellow)">
      <div class="tile-head" style="font-size:38px;line-height:46px;margin-top:4px">Register<br>YOUR<br>WATCH</div>
      <div class="tile-note">Lorem Ipsum is<br>simply dummy text of the</div>
    </div>

    <div class="abs tile-photo" style="left:749px;width:122px;background:radial-gradient(circle,#9a9a9a,#2a2a2a 70%,#000)" role="img" aria-label="Scattered crystal gemstones"></div>
    <div class="abs tile tile-text" style="left:871px;width:168px;background:var(--orange)">
      <div class="tile-head" style="font-size:34px;margin-top:4px">Repair</div>
      <div class="tile-head" style="font-size:22px;line-height:26px">Maintenance<br>And<br>Warranty Info</div>
      <div class="tile-note">Lorem Ipsum is<br>simply dummy text of the</div>
    </div>
  </section>

  <section class="abs register">
    <h2 class="abs reg-title" style="font-weight:400">REGISTER to find out about new<br><span>WATCH COLLECTIONS</span></h2>
    <div class="abs field" style="left:17px;width:197px">Enter your email address</div>
    <div class="abs field" style="left:226px;width:199px;padding-left:10px">Enter Password</div>
    <div class="abs login">LOGIN NOW</div>
    <div class="abs signup"><span>Yet Not Registerd?</span> Signup</div>
  </section>

  <section class="social-links">
    <div class="abs social" style="top:733px"><div class="social-box" style="background:var(--folk)"></div><span class="social-name" style="color:var(--folk)">FOLKSPACE</span></div>
    <div class="abs social" style="top:794px"><div class="social-box" style="background:var(--chirp)"></div><span class="social-name" style="color:var(--chirp)">CHIRPLINE</span></div>
    <div class="abs social" style="top:856px"><div class="social-box" style="background:var(--reel)"></div><span class="social-name" style="color:var(--reel)">REELHALL</span></div>
  </section>

  <footer class="abs footer">
    <div class="abs footer-links">
      <span>HOME</span><span>|</span><span>CONTACT US</span><span>&nbsp;&nbsp;|</span><span>TERMS OF SERVICE</span><span>|</span><span>REFUND POLICY</span><span>|</span><span>PRIVACY POLICY</span>
    </div>
    <div class="abs footer-copy">Copyright 2013 &nbsp;| &nbsp;<span>All Rights</span> &nbsp;Belthor.com</div>
  </footer>
  <div class="abs footer-base"></div>
</div>
</body>
</html>
```